mobile physiotherapy for the elderly

i have include a logo for you to use
i have included important info to include on the flyer.
the flyer will be a dl size
the flyer will be used for getting new clients at a health expo. it needs to be eye catching as i may be using it as a vertical banner at my stall
big words and illustations that take up most of the design

Target Market(s)

veterans of war, mainly over 55years of age

Industry/Entity Type

Healthcare

Font styles to use
Sans Serif
Decorative
Script
Other font styles liked:
• i would like the slogan in a handwriting type font, but not running-writing or overly formal fonts

Colors

Designer to choose colors to be used in the design.

Requirements
Must have
• i would like to incorporate my logo woth the slogan " we come to you!" i want this slogan to be very prominent as i may want to use this as a vertical banner at a health expo
• i would like to see an illustrated (Cartoon-like) car on one side and a house on the other, being joined together by a winding road.
Nice to have
• potentially something with a map in the background or as the background or the whole flyer. We are located and work in sydney, australia. so if you can tastefully include a map that would be great. it does not need to be a map of sydney if you dont feel like it works
Should not have
• no photographs
• no people

```html
<!DOCTYPE html>
<html lang="en">
<head>
<meta charset="utf-8">
<title>Hearth Physiotherapy – We Come To You</title>
<link rel="stylesheet" href="https://fonts.googleapis.com/css2?family=Londrina+Solid:wght@900&family=Patrick+Hand&family=Barlow+Semi+Condensed:wght@700&family=Kalam:wght@700&family=Nunito:wght@800&display=swap">
<style>
  :root {
    --surround: #000000;
    --mint-top: #c4ebe6;
    --teal: #45bcaf;
    --teal-deep: #36b0a3;
    --navy: #0d3470;
    --slogan: #1d3f78;
    --logo-slate: #5b7091;
    --ink: #1e1e1e;
    --white: #ffffff;
    --grass: #2f8a2c;
    --grass-dark: #1f6a1f;
    --sky-cloud: #d9efee;
    --road-grey: #a7a9ab;
  }
  * { margin: 0; padding: 0; box-sizing: border-box; }
  html, body {
    width: 1200px; height: 2579px; overflow: hidden;
    background: var(--surround);
  }
  .banner {
    position: absolute; left: 118px; top: 156px;
    width: 964px; height: 2264px; overflow: hidden;
    background: linear-gradient(180deg, var(--mint-top) 0%, var(--teal) 22%, var(--teal-deep) 55%, var(--teal-deep) 100%);
  }
  .scene {
    position: absolute; left: 0; top: 1260px; width: 964px; height: 1004px;
    background:
      radial-gradient(ellipse 420px 260px at 150px 640px, var(--white) 0%, var(--white) 55%, rgba(255,255,255,0) 100%),
      radial-gradient(ellipse 360px 300px at 820px 520px, var(--grass-dark) 0%, rgba(31,106,31,0) 100%),
      radial-gradient(ellipse 280px 180px at 760px 280px, #e9ecec 0%, rgba(233,236,236,0) 100%),
      radial-gradient(ellipse 300px 90px at 720px 110px, var(--sky-cloud) 0%, rgba(217,239,238,0) 100%),
      linear-gradient(180deg, rgba(54,176,163,0) 0%, rgba(54,176,163,0) 28%, #58a548 40%, var(--grass) 52%, #c9d6c6 66%, var(--road-grey) 82%, #dcdcdc 100%);
  }
  .brand {
    position: absolute; left: 88px; top: 51px; width: 620px;
    font-family: "Nunito", sans-serif; font-weight: 800; color: var(--logo-slate);
    line-height: 1;
  }
  .brand__name { display: block; font-size: 160px; letter-spacing: 6px; }
  .brand__sub { display: block; font-size: 50px; letter-spacing: 10px; margin-top: 4px; text-transform: uppercase; }
  .slogan {
    position: absolute; left: 96px; top: 305px; width: 860px;
    font-family: "Londrina Solid", "Kalam", cursive; font-weight: 900;
    color: var(--slogan); text-transform: uppercase; line-height: 0.92;
    font-size: 232px; letter-spacing: 8px;
  }
  .slogan__line { display: block; }
  .slogan__line--two { margin-left: 10px; }
  .pitch {
    position: absolute; left: 60px; top: 760px; width: 880px;
    font-family: "Patrick Hand", cursive; color: var(--white);
    font-size: 48px; line-height: 1.17;
  }
  .pitch span { display: block; }
  .pitch .l1 { margin-left: 68px; }
  .pitch .l2 { margin-left: 160px; }
  .pitch .l3 { margin-left: 20px; }
  .pitch .l4 { margin-left: 225px; }
  .pitch .l5 { margin-left: 40px; }
  .services-title {
    position: absolute; left: 42px; top: 1105px;
    font-family: "Kalam", cursive; font-weight: 700; color: var(--ink);
    font-size: 62px; line-height: 1;
  }
  .services {
    position: absolute; left: 42px; top: 1185px; list-style: none;
  }
  .services__item {
    height: 46px; margin-bottom: 8px; background: var(--navy); color: var(--white);
    font-family: "Patrick Hand", cursive; font-size: 35px; line-height: 46px;
    padding-left: 30px;
    clip-path: polygon(0 0, 100% 0, calc(100% - 30px) 100%, 0 100%);
  }
  .services__item:nth-child(1) { width: 498px; }
  .services__item:nth-child(2) { width: 472px; }
  .services__item:nth-child(3) { width: 446px; }
  .services__item:nth-child(4) { width: 420px; }
  .services__item:nth-child(5) { width: 395px; }
  .services__item:nth-child(6) { width: 370px; }
  .contact { position: absolute; left: 42px; top: 1672px; }
  .contact__lead, .contact__tail {
    font-family: "Kalam", cursive; font-weight: 700; color: var(--ink);
    font-size: 50px; line-height: 1; margin-left: 14px;
  }
  .contact__phone {
    display: inline-block; margin: 12px 0 10px; padding: 0 14px;
    width: 614px; height: 100px; line-height: 100px; background: var(--navy); color: var(--white);
    font-family: "Barlow Semi Condensed", sans-serif; font-weight: 700;
    font-size: 108px; letter-spacing: 2px; white-space: nowrap;
  }
</style>
</head>
<body>
  <main class="banner">
    <div class="scene" role="img" aria-label="Illustration area: a winding grey road through green hills leading from a silver van in the foreground up to a white house with a green roof, with pine trees and soft clouds"></div>

    <div class="brand">
      <span class="brand__name">Hearth</span>
      <span class="brand__sub">Physiotherapy</span>
    </div>

    <h1 class="slogan">
      <span class="slogan__line">We Come</span>
      <span class="slogan__line slogan__line--two">To You!</span>
    </h1>

    <p class="pitch">
      <span class="l1">Trained and experienced professionals</span>
      <span class="l2">evaluate your rehabilitation needs</span>
      <span class="l3">Specialised treatment programs to</span>
      <span class="l4">suit individual needs One-on-one</span>
      <span class="l5">physiotherapy treatment in your home</span>
    </p>

    <h2 class="services-title">How we can help:</h2>
    <ul class="services">
      <li class="services__item">Post-surgical Rehabilitation</li>
      <li class="services__item">Geriatric Care</li>
      <li class="services__item">Postural Analysis</li>
      <li class="services__item">Neurological Disorders</li>
      <li class="services__item">Aid prescription</li>
      <li class="services__item">Pain management</li>
    </ul>

    <div class="contact">
      <p class="contact__lead">Call us on</p>
      <p class="contact__phone">0400 123 456</p>
      <p class="contact__tail">for further information</p>
    </div>
  </main>
</body>
</html>
```